Business Card Design Project

New Private residential substance abuse treatment facility in Mapleton, UT. Facility located in elegant 11,000 home with stunning views of the mountains. Wish to incorporate colored logo. Business name- Birchwell Harbor Wellness. Facility is Tudor style with traditional furnishings, an overhead picture is attached. Lettering in a simple scroll or old english style. Must be easy to read with clear moderetly large font.
Updates

It seems the project time frame listed was not correct- it is a week.

Target Market(s)

Adults 18 and over with substance abuse issues requiring residential rehabilitation. Referral base are medical/mental health professionals, families and community agencies.

Industry/Entity Type

Residential

Colors
9bcb3b
fece3e
fbee3f

Requirements
Must have
• Clear and easy to read, professional and upscale presentation. Need logo, name, title, address, phone, fax and web page address. May add slogan later. Use same font as logo.
Nice to have
• Logo has a green mountain and a gold maple leaf so a nature themed element may work. Want to promote peaceful grounded image. Logo attached.
Should not have
• No tiny or complicated font. No modern or tech looking images. No light colored fonts.

```html
<!DOCTYPE html>
<html lang="en">
<head>
<meta charset="utf-8">
<title>Birchwell Harbor Wellness – Business Card</title>
<link href="https://fonts.googleapis.com/css2?family=Open+Sans:wght@600;700&display=swap" rel="stylesheet">
<style>
  :root {
    --backdrop: #e6e6e6;
    --card: #ffffff;
    --forest: #3d6b2a;
    --gold: #d9a524;
    --ink: #3a3a3a;
  }
  * { margin: 0; padding: 0; box-sizing: border-box; }
  html, body {
    width: 1200px;
    height: 800px;
    overflow: hidden;
    background: var(--backdrop);
    font-family: "Open Sans", Arial, sans-serif;
  }
  .stage {
    width: 1200px;
    height: 800px;
    display: flex;
    align-items: center;
    justify-content: center;
  }
  .business-card {
    position: relative;
    width: 840px;
    height: 480px;
    background: var(--card);
    border-radius: 44px;
    overflow: hidden;
    box-shadow: 0 6px 18px rgba(0,0,0,0.12);
  }
  .card-bands {
    position: absolute;
    inset: 0;
    width: 100%;
    height: 100%;
  }
  .brand {
    position: absolute;
    top: 64px;
    left: 0;
    right: 0;
    display: flex;
    align-items: center;
    justify-content: center;
    gap: 14px;
    padding-left: 90px;
  }
  .brand-dot {
    width: 30px;
    height: 30px;
    border-radius: 50%;
    background: var(--gold);
  }
  .brand-name {
    font-size: 34px;
    font-weight: 700;
    color: var(--forest);
    letter-spacing: 0.5px;
  }
  .identity {
    position: absolute;
    top: 218px;
    left: 120px;
    width: 330px;
    text-align: right;
  }
  .person-name {
    font-size: 50px;
    font-weight: 700;
    color: var(--forest);
    line-height: 1.05;
    letter-spacing: 0.5px;
  }
  .person-title {
    font-size: 14px;
    font-weight: 700;
    color: var(--forest);
    margin-top: 4px;
    letter-spacing: 0.5px;
  }
  .divider {
    position: absolute;
    top: 192px;
    left: 478px;
    width: 3px;
    height: 118px;
    background: var(--forest);
  }
  .contact-list {
    position: absolute;
    top: 196px;
    left: 500px;
    list-style: none;
    font-size: 16px;
    font-weight: 700;
    color: var(--forest);
    line-height: 1.3;
    letter-spacing: 0.3px;
  }
</style>
</head>
<body>
<main class="stage">
  <section class="business-card" aria-label="Business card, Birchwell Harbor Wellness">
    <svg class="card-bands" viewBox="0 0 840 480" preserveAspectRatio="none" aria-hidden="true">
      <path d="M40 480 C 300 455, 600 360, 840 278 L 840 312 C 620 392, 330 470, 120 480 Z" fill="var(--gold)"/>
      <path d="M0 480 L 0 468 C 300 460, 600 380, 840 312 L 840 480 Z" fill="var(--forest)"/>
    </svg>

    <header class="brand">
      <span class="brand-dot"></span>
      <span class="brand-name">Birchwell Harbor Wellness</span>
    </header>

    <div class="identity">
      <h1 class="person-name">OWEN HALE</h1>
      <p class="person-title">TITLE GOES HERE</p>
    </div>

    <span class="divider"></span>

    <ul class="contact-list">
      <li>ADRESSE:</li>
      <li>PHONE:</li>
      <li>FAX:</li>
      <li>WEBSITE:</li>
    </ul>
  </section>
</main>
</body>
</html>
```